水草を入れるパック(ビニール)に直接印刷するため、中身が見えるようなデザインで、ホームセンターの中にあるペットショップなどに展開するため、手に取りやすく、
また商品の詳細もわかるようなデザイン(メダカのイラスト入れてもOKです。)を
希望いたします。
※表には「ソヨギの森草」をわかりやすく、目立つように。
(中身のまつもも前から見てわかるように)
※裏面に入れる
・JANコード 4513870294615
・仕様上の注意
使用する前にまつもに付着している生体(貝など)必ず水洗いをしてからご使用ください。
直射日光が当たるところは避けてください。
適正温度15℃~25℃ を必ず入れてください。
サイズ 縦22㎝×横12㎝
黄・オレンジ系、青系、水色系
• イラストレーター形式 (.ai)
• フォトショップ形式 (.psd)
使用上の注意で印刷する文面はこちらでお願い致します。
・水草に貝等付着している場合があります。
・使用する前は必ず水道水ですすいでから使用してください。
・高価な魚・エビ・貝等には仕様をお控えください。
(水草を使用し、お客様の魚等に支障が出た場合では当店は一切の保証は致しかねます。)
・直射日光はお控えください。
・観賞魚用水槽に使用する以外お控えください。
・これは食べ物ではありません。(サラダでも御座いません。)
・小さなお子様の手の届かないところには置かないで下さい。
よろしくお願い致します。

デザインにインパクトがあり、どのような商品か伝わりやすく、色んな年齢層でも手に取ってもらいやすいデザインだと思ったので、今回選ばせていただきました。

皆様の作品は、どれも素晴らしく選ぶのに非常に悩みました。また依頼した際は、よろしくお願い致します。ご参加いただき、ありがとうございました。

```html
<!DOCTYPE html>
<html lang="ja">
<head>
<meta charset="utf-8">
<title>ソヨギの森草 マツモ</title>
<link rel="stylesheet" href="https://fonts.googleapis.com/css2?family=Noto+Sans+JP:wght@500;700;900&family=Noto+Serif+JP:wght@700;900&display=swap">
<style>
  :root {
    --bg: #f4f6f8;
    --silver-top: #eef1f3;
    --silver-bottom: #c9d2d8;
    --window-top: #e6f0ea;
    --window-mid: #a9cfa0;
    --window-bottom: #c4e3ee;
    --plant-core: #3f8f2c;
    --plant-mid: #6fae4f;
    --plant-edge: #a8d08e;
    --green-deep: #2f8f3f;
    --green: #49a64a;
    --aqua: #7fcde6;
    --aqua-light: #c7ecf6;
    --navy: #1f418f;
    --navy-dark: #15306e;
    --sky-text: #9fdcff;
    --white: #ffffff;
    --badge-green: #2d9a3a;
  }
  * { margin: 0; padding: 0; box-sizing: border-box; }
  html, body {
    width: 720px; height: 1200px; overflow: hidden;
    background: var(--bg);
  }
  .pack {
    position: relative;
    width: 720px; height: 1200px;
    overflow: hidden;
    background: linear-gradient(180deg, var(--silver-top), var(--silver-bottom));
    font-family: "Noto Sans JP", sans-serif;
  }
  .pack-shapes { position: absolute; inset: 0; }
  .vertical { position: absolute; writing-mode: vertical-rl; white-space: nowrap; }
  .tagline {
    left: 606px; top: 70px;
    font-family: "Noto Serif JP", serif; font-weight: 900;
    font-size: 48px; letter-spacing: 2px; color: var(--white);
    text-shadow: 0 2px 4px rgba(0,60,20,.45);
  }
  .float-note {
    left: 556px; top: 420px;
    font-weight: 700; font-size: 20px; color: var(--white);
    text-shadow: 0 1px 3px rgba(0,60,20,.5);
  }
  .badge {
    position: absolute; left: 360px; top: 280px;
    width: 176px; height: 130px;
    transform: rotate(-10deg);
    background: var(--white);
    border: 4px solid var(--badge-green);
    border-radius: 50%;
    display: flex; flex-direction: column; align-items: center; justify-content: center;
    box-shadow: 0 3px 8px rgba(0,0,0,.2);
  }
  .badge-lead { font-size: 20px; font-weight: 700; color: var(--badge-green); }
  .badge-main {
    margin-top: 4px; padding: 0 14px;
    font-size: 46px; font-weight: 900; line-height: 1.15;
    color: var(--white); background: var(--badge-green); border-radius: 8px;
  }
  .brand-name {
    left: 486px; top: 420px;
    font-family: "Noto Serif JP", serif; font-weight: 900;
    font-size: 54px; letter-spacing: 1px; color: var(--white);
    text-shadow: 0 3px 6px rgba(0,50,30,.5);
  }
  .product-name {
    left: 582px; top: 650px;
    font-family: "Noto Serif JP", serif; font-weight: 900;
    font-size: 118px; line-height: 1; color: var(--white);
    text-shadow: 0 4px 8px rgba(0,60,90,.45);
  }
  .product-note {
    left: 462px; top: 850px;
    font-weight: 700; font-size: 26px; line-height: 1.45;
    color: var(--white);
    text-shadow: 0 1px 3px rgba(0,60,90,.55);
  }
  .band-copy {
    position: absolute; left: 188px; top: 200px;
    display: flex; flex-direction: row-reverse; gap: 14px;
    transform: rotate(9deg); transform-origin: top right;
  }
  .band-copy .vertical { position: static; }
  .band-copy-lead { font-size: 30px; font-weight: 700; color: var(--sky-text); margin-top: 0; }
  .band-copy-main { font-size: 36px; font-weight: 900; color: var(--white); margin-top: 120px; }
</style>
</head>
<body>
<main class="pack">
  <svg class="pack-shapes" width="720" height="1200" viewBox="0 0 720 1200">
    <defs>
      <linearGradient id="windowFill" x1="0" y1="0" x2="0" y2="1">
        <stop offset="0" stop-color="var(--window-top)"/>
        <stop offset=".5" stop-color="var(--window-mid)"/>
        <stop offset="1" stop-color="var(--window-bottom)"/>
      </linearGradient>
      <radialGradient id="photoFill" cx=".5" cy=".42" r=".55">
        <stop offset="0" stop-color="var(--plant-core)"/>
        <stop offset=".55" stop-color="var(--plant-mid)"/>
        <stop offset="1" stop-color="var(--plant-edge)" stop-opacity="0"/>
      </radialGradient>
      <linearGradient id="panelFill" x1="0" y1="0" x2="0" y2="1">
        <stop offset="0" stop-color="var(--green-deep)"/>
        <stop offset=".4" stop-color="var(--green)"/>
        <stop offset=".75" stop-color="var(--aqua)"/>
        <stop offset="1" stop-color="var(--aqua-light)"/>
      </linearGradient>
      <linearGradient id="bandFill" x1="0" y1="0" x2="1" y2="0">
        <stop offset="0" stop-color="var(--navy-dark)"/>
        <stop offset="1" stop-color="var(--navy)"/>
      </linearGradient>
    </defs>
    <rect class="clear-window" x="0" y="120" width="520" height="1080" fill="url(#windowFill)"/>
    <ellipse class="product-photo" role="img" aria-label="透明な窓越しに見えるマツモの水草と、その下を泳ぐメダカ"
             cx="300" cy="620" rx="300" ry="420" fill="url(#photoFill)"/>
    <path class="side-panel" d="M380 0 L720 0 L720 1200 L470 1200 C520 900 430 620 470 360 C490 220 420 90 380 0 Z"
          fill="url(#panelFill)"/>
    <path class="copy-band" d="M200 60 L350 60 L200 1200 L50 1200 Z" fill="url(#bandFill)" opacity=".95"/>
  </svg>

  <div class="band-copy">
    <p class="vertical band-copy-lead">どんな水槽にも対応できる</p>
    <p class="vertical band-copy-main">適応能力の高い水草です</p>
  </div>

  <h2 class="vertical tagline">根を持たず育つ草</h2>

  <div class="badge">
    <span class="badge-lead">初心者の方でも</span>
    <span class="badge-main">簡単</span>
  </div>

  <p class="vertical float-note">浮かべるだけの簡単飼育!</p>
  <p class="vertical brand-name">ソヨギの森草</p>
  <h1 class="vertical product-name">マツモ</h1>
  <p class="vertical product-note">マツモがメダカの<br>飼育・産卵を<br>お助けします</p>
</main>
</body>
</html>
```